k eLiquid Label

We are an electronic cigarette eLiquid manufacturer with an outdated label design which needs to be updated and become more modern. All information listed on the label cannot be changed or removed.

There are 4 colour coding on the labels that cannot change.
0mg is white
12mg is yellow
18mg is blue
24mg is red

We prefer a blue type background however are not committed to it with the proper design however if a new colour is chosen it must compliment the colour band for each colour coding

The "dots" on the front of the bottle need to be larger.

The "V" on the front needs to be in this font however we can accept slight changes to it for effect.

Issues we are facing:
The 0mg and the 18mg look too close in colour and need to be completely different in colouring.

The background colouring is too dark and you cannot see the 50/50 in the watermark.

Reason: We have not received a design which is suitable to our needs. We have see a few close ones however not exact. Thanks

Reason: I was forced to go out of country for a family emergency and to be fair I am extending the deadline

```html
<!DOCTYPE html>
<html lang="en">
<head>
<meta charset="utf-8">
<title>k eLiquid Label – Sweet Tobacco</title>
<link rel="stylesheet" href="https://fonts.googleapis.com/css2?family=PT+Sans+Narrow:wght@400;700&family=Roboto+Condensed:wght@700;900&display=swap">
<style>
  :root{
    --stage-top:#2a3590;
    --stage-bottom:#1b1d33;
    --label-blue:#3591d3;
    --label-blue-deep:#2580c6;
    --watermark:rgba(190,225,250,.42);
    --ink:#0c1a2c;
    --paper:#ffffff;
    --band-zero:#ffffff;
    --band-12:#f6ea1e;
    --band-18:#252a6c;
    --band-24:#e0242b;
    --hazard:#f4e21a;
  }
  *{box-sizing:border-box;margin:0;padding:0}
  html,body{width:1200px;height:1000px;overflow:hidden}
  body{
    background:linear-gradient(150deg,var(--stage-top) 0%,#24296a 45%,var(--stage-bottom) 100%);
    font-family:"PT Sans Narrow",sans-serif;
    position:relative;
  }
  .label{
    position:absolute;left:248px;width:705px;height:236px;
    background:var(--label-blue);
    color:var(--ink);
    overflow:hidden;
    box-shadow:0 4px 10px rgba(0,0,0,.45);
  }
  .label--zero{top:0;--band:var(--band-zero);--badge-ink:#ffffff;--badge-fill:var(--label-blue-deep)}
  .label--12{top:252px;--band:var(--band-12);--badge-ink:#1a2a6c;--badge-fill:var(--band-12)}
  .label--18{top:504px;--band:var(--band-18);--badge-ink:#ffffff;--badge-fill:var(--band-18)}
  .label--24{top:753px;--band:var(--band-24);--badge-ink:#ffffff;--badge-fill:var(--band-24)}

  .label__top-band{position:absolute;left:0;top:0;width:100%;height:6px;background:var(--band)}
  .label__swirl{
    position:absolute;left:0;top:6px;width:100%;height:190px;
    background:
      radial-gradient(ellipse 60% 40% at 20% 40%,rgba(255,255,255,.12),transparent 70%),
      radial-gradient(ellipse 50% 45% at 85% 30%,rgba(255,255,255,.18),transparent 70%);
  }
  .label__footer{
    position:absolute;left:0;top:196px;width:100%;height:40px;
    background:var(--label-blue-deep);
    border-top:6px solid var(--band);
    color:var(--paper);
    font-size:12px;line-height:13px;white-space:nowrap;
  }
  .footer__fr{position:absolute;right:470px;top:5px;text-align:right}
  .footer__size{position:absolute;right:256px;top:5px;text-align:right;font-family:"Roboto Condensed",sans-serif;font-weight:700;font-size:12.5px;line-height:14px}
  .footer__en{position:absolute;left:470px;top:5px}

  .watermark{
    position:absolute;left:250px;top:8px;width:210px;text-align:center;
    font-family:"Roboto Condensed",sans-serif;font-weight:900;
    font-size:66px;line-height:60px;letter-spacing:0;
    color:var(--watermark);white-space:nowrap;
  }
  .watermark span{display:block;height:60px}

  .brand{
    position:absolute;left:255px;top:46px;width:200px;text-align:center;
    font-family:"Roboto Condensed",sans-serif;font-weight:700;color:var(--paper);
    white-space:nowrap;
  }
  .brand__name{font-size:44px;line-height:46px}
  .brand__flavour{font-size:27px;line-height:30px;margin-top:30px;letter-spacing:.5px}

  .copy{position:absolute;top:10px;font-size:12px;line-height:15.8px;white-space:nowrap}
  .copy b{font-weight:700}
  .copy--fr{right:470px;text-align:right}
  .copy--en{left:470px}

  .hazard{position:absolute;left:6px;top:6px}

  .batch{
    position:absolute;left:470px;top:171px;width:234px;height:24px;
    background:var(--paper);font-size:12px;padding:5px 0 0 4px;white-space:nowrap;
  }
  .batch span+span{margin-left:68px}

  .badge{
    position:absolute;left:333px;top:178px;width:44px;height:44px;border-radius:50%;
    background:var(--badge-fill);border:4px solid var(--band);
    box-shadow:0 0 0 2px var(--label-blue);
    display:flex;align-items:center;justify-content:center;
    font-family:"Roboto Condensed",sans-serif;font-weight:700;color:var(--badge-ink);
    font-size:19px;
  }
  .label--zero .badge{font-size:12px}
</style>
</head>
<body>

<article class="label label--zero">
  <div class="label__top-band"></div>
  <div class="label__swirl" role="img" aria-label="Soft flowing light swirl lines across the label background"></div>
  <div class="watermark" aria-hidden="true"><span>50/50</span><span>50/50</span><span>50/50</span></div>
  <svg class="hazard" width="38" height="34" viewBox="0 0 38 34" aria-label="Hazard warning"><path d="M19 2 L36 32 H2 Z" fill="var(--hazard)" stroke="#111" stroke-width="2.5" stroke-linejoin="round"/><circle cx="19" cy="21" r="5" fill="#111"/></svg>
  <div class="copy copy--fr"><b>CONTENIR NOCIF</b><br>Ne pas avaler.<br>Ne pas mettre dans les yeux ou sur la peau ou les<br>vêtements.<br>Tenir hors de portée des enfants et des animaux.<br><b>INGRÉDIENTS:</b> Propylène Glycol, Glycérine, Alcool de<br>Qualité Alimentaire, Arômes Naturel et Artificiels.<br><b>En cas d’ingestion consulter centre<br>antipoison ou un medécin immédiatement.<br>Peux contenir de noix.</b></div>
  <div class="brand"><div class="brand__name">k eLiquid</div><div class="brand__flavour">SWEET TOBACCO</div></div>
  <div class="copy copy--en"><b>WARNING CONTENTS HARMFUL</b><br>Do not swallow.<br>Do not get in eyes or on skin or clothing.<br>Keep out of reach of children and pets.<br><b>IN GREDIENTS:</b> Propylene Glycol, Vegetable<br>Glycerin, Food Grade Alcohol, Natural and Artificial<br>Flavours.<br><b>If swallowed consult poison control centre or<br>a doctor immediately.<br>May contain nuts.</b></div>
  <div class="batch"><span>BATCH :</span><span>EXPIRES :</span></div>
  <footer class="label__footer">
    <div class="footer__fr">Produit et emballlé exclusivement pour:<br>5521930 Ontario Inc, Millbrook ON, L0A 1G0</div>
    <div class="footer__size">30 ml<br>E-LIQUID</div>
    <div class="footer__en">Produced and Packaged exclusively for :<br>5521930 Ontario Inc, Millbrook ON, L0A 1G0</div>
  </footer>
  <div class="badge">ZERO</div>
</article>

<article class="label label--12">
  <div class="label__top-band"></div>
  <div class="label__swirl" role="img" aria-label="Soft flowing yellow and light swirl lines across the label background"></div>
  <div class="watermark" aria-hidden="true"><span>50/50</span><span>50/50</span><span>50/50</span></div>
  <svg class="hazard" width="38" height="34" viewBox="0 0 38 34" aria-label="Hazard warning"><path d="M19 2 L36 32 H2 Z" fill="var(--hazard)" stroke="#111" stroke-width="2.5" stroke-linejoin="round"/><circle cx="19" cy="21" r="5" fill="#111"/></svg>
  <div class="copy copy--fr"><b>CONTENIR NOCIF</b><br>Ne pas avaler.<br>Ne pas mettre dans les yeux ou sur la peau ou les<br>vêtements.<br>Tenir hors de portée des enfants et des animaux.<br><b>INGRÉDIENTS:</b> Propylène Glycol, Glycérine, Alcool de<br>Qualité Alimentaire, Arômes Naturel et Artificiels.<br><b>En cas d’ingestion consulter centre<br>antipoison ou un medécin immédiatement.<br>Peux contenir de noix.</b></div>
  <div class="brand"><div class="brand__name">k eLiquid</div><div class="brand__flavour">SWEET TOBACCO</div></div>
  <div class="copy copy--en"><b>WARNING CONTENTS HARMFUL</b><br>Do not swallow.<br>Do not get in eyes or on skin or clothing.<br>Keep out of reach of children and pets.<br><b>IN GREDIENTS:</b> Propylene Glycol, Vegetable<br>Glycerin, Food Grade Alcohol, Natural and Artificial<br>Flavours.<br><b>If swallowed consult poison control centre or<br>a doctor immediately.<br>May contain nuts.</b></div>
  <div class="batch"><span>BATCH :</span><span>EXPIRES :</span></div>
  <footer class="label__footer">
    <div class="footer__fr">Produit et emballlé exclusivement pour:<br>5521930 Ontario Inc, Millbrook ON, L0A 1G0</div>
    <div class="footer__size">30 ml<br>E-LIQUID</div>
    <div class="footer__en">Produced and Packaged exclusively for :<br>5521930 Ontario Inc, Millbrook ON, L0A 1G0</div>
  </footer>
  <div class="badge">12</div>
</article>

<article class="label label--18">
  <div class="label__top-band"></div>
  <div class="label__swirl" role="img" aria-label="Soft flowing navy and light swirl lines across the label background"></div>
  <div class="watermark" aria-hidden="true"><span>50/50</span><span>50/50</span><span>50/50</span></div>
  <svg class="hazard" width="38" height="34" viewBox="0 0 38 34" aria-label="Hazard warning"><path d="M19 2 L36 32 H2 Z" fill="var(--hazard)" stroke="#111" stroke-width="2.5" stroke-linejoin="round"/><circle cx="19" cy="21" r="5" fill="#111"/></svg>
  <div class="copy copy--fr"><b>CONTENIR NOCIF</b><br>Ne pas avaler.<br>Ne pas mettre dans les yeux ou sur la peau ou les<br>vêtements.<br>Tenir hors de portée des enfants et des animaux.<br><b>INGRÉDIENTS:</b> Propylène Glycol, Glycérine, Alcool de<br>Qualité Alimentaire, Arômes Naturel et Artificiels.<br><b>En cas d’ingestion consulter centre<br>antipoison ou un medécin immédiatement.<br>Peux contenir de noix.</b></div>
  <div class="brand"><div class="brand__name">k eLiquid</div><div class="brand__flavour">SWEET TOBACCO</div></div>
  <div class="copy copy--en"><b>WARNING CONTENTS HARMFUL</b><br>Do not swallow.<br>Do not get in eyes or on skin or clothing.<br>Keep out of reach of children and pets.<br><b>IN GREDIENTS:</b> Propylene Glycol, Vegetable<br>Glycerin, Food Grade Alcohol, Natural and Artificial<br>Flavours.<br><b>If swallowed consult poison control centre or<br>a doctor immediately.<br>May contain nuts.</b></div>
  <div class="batch"><span>BATCH :</span><span>EXPIRES :</span></div>
  <footer class="label__footer">
    <div class="footer__fr">Produit et emballlé exclusivement pour:<br>5521930 Ontario Inc, Millbrook ON, L0A 1G0</div>
    <div class="footer__size">30 ml<br>E-LIQUID</div>
    <div class="footer__en">Produced and Packaged exclusively for :<br>5521930 Ontario Inc, Millbrook ON, L0A 1G0</div>
  </footer>
  <div class="badge">18</div>
</article>

<article class="label label--24">
  <div class="label__top-band"></div>
  <div class="label__swirl" role="img" aria-label="Soft flowing red and light swirl lines across the label background"></div>
  <div class="watermark" aria-hidden="true"><span>50/50</span><span>50/50</span><span>50/50</span></div>
  <svg class="hazard" width="38" height="34" viewBox="0 0 38 34" aria-label="Hazard warning"><path d="M19 2 L36 32 H2 Z" fill="var(--hazard)" stroke="#111" stroke-width="2.5" stroke-linejoin="round"/><circle cx="19" cy="21" r="5" fill="#111"/></svg>
  <div class="copy copy--fr"><b>CONTENIR NOCIF</b><br>Ne pas avaler.<br>Ne pas mettre dans les yeux ou sur la peau ou les<br>vêtements.<br>Tenir hors de portée des enfants et des animaux.<br><b>INGRÉDIENTS:</b> Propylène Glycol, Glycérine, Alcool de<br>Qualité Alimentaire, Arômes Naturel et Artificiels.<br><b>En cas d’ingestion consulter centre<br>antipoison ou un medécin immédiatement.<br>Peux contenir de noix.</b></div>
  <div class="brand"><div class="brand__name">k eLiquid</div><div class="brand__flavour">SWEET TOBACCO</div></div>
  <div class="copy copy--en"><b>WARNING CONTENTS HARMFUL</b><br>Do not swallow.<br>Do not get in eyes or on skin or clothing.<br>Keep out of reach of children and pets.<br><b>IN GREDIENTS:</b> Propylene Glycol, Vegetable<br>Glycerin, Food Grade Alcohol, Natural and Artificial<br>Flavours.<br><b>If swallowed consult poison control centre or<br>a doctor immediately.<br>May contain nuts.</b></div>
  <div class="batch"><span>BATCH :</span><span>EXPIRES :</span></div>
  <footer class="label__footer">
    <div class="footer__fr">Produit et emballlé exclusivement pour:<br>5521930 Ontario Inc, Millbrook ON, L0A 1G0</div>
    <div class="footer__size">30 ml<br>E-LIQUID</div>
    <div class="footer__en">Produced and Packaged exclusively for :<br>5521930 Ontario Inc, Millbrook ON, L0A 1G0</div>
  </footer>
  <div class="badge">24</div>
</article>

</body>
</html>
```